Business Card for new Architectural Firm

I intend to practice in a rural mountain community in upstate NY, focusing on residential and light commercial projects, including second home / vacation properties. I wish to convey a feeling of rural outdoorsy modernity.

Color is important - bold and urbane. Secondary or tertiary colors preferred.

Font is important, idiosyncratic is ok

Optionally, I may choose to use the name Brackenfold Studio. If used as part of your design, all of the Must Haves are still required.

Images uploaded are logos I like

Industry/Entity Type

Residential

Contact Information for Business Card

Caldwell Prusinski
Architect (This word should stand alone or be associated with my name - not license number)
NY License No. 582163
caldwell@designcpx.com
607 394 2858

Font styles to use
Sans Serif
Decorative

Requirements
Must have
• Whatever files I need to best utilize your design
• PDF
• JPG
• EPS
• Vectorwhatsit
Nice to have
• Logo or element that can be incorporated into other print material.
• Could be a font based card
Should not have
• no clip art
• No templates
• no floor plans
• no building photographs

```html
<!DOCTYPE html>
<html lang="en">
<head>
<meta charset="utf-8">
<title>Caldwell Prusinski Architect – Business Card</title>
<link rel="stylesheet" href="https://fonts.googleapis.com/css2?family=Inter:ital,wght@0,300;0,400;1,200;1,300&display=swap">
<style>
  :root {
    --backdrop: #1c1c1e;
    --card-top: #4b74b2;
    --card-mid: #2f3f82;
    --card-bottom: #1a1b50;
    --ink: #ffffff;
    --ink-soft: rgba(255,255,255,0.86);
    --rule: rgba(255,255,255,0.28);
  }
  * { margin: 0; padding: 0; box-sizing: border-box; }
  html, body {
    width: 1200px; height: 900px; overflow: hidden;
    background: var(--backdrop);
    font-family: "Inter", "Helvetica Neue", Arial, sans-serif;
  }
  .sheet { position: relative; width: 1200px; height: 900px; }
  .card {
    position: absolute;
    left: 311px;
    width: 595px; height: 339px;
    background: linear-gradient(180deg, var(--card-top) 0%, var(--card-mid) 50%, var(--card-bottom) 100%);
    color: var(--ink);
  }
  .card--top { top: 86px; }
  .card--bottom { top: 474px; }
  .identity {
    position: absolute;
    left: 127px; top: 136px;
    width: 342px;
    text-align: center;
  }
  .name {
    font-size: 35px;
    line-height: 40px;
    letter-spacing: 0.5px;
    white-space: nowrap;
  }
  .name__first { font-weight: 400; }
  .name__last { font-weight: 200; font-style: italic; color: var(--ink-soft); }
  .title {
    font-size: 16px;
    font-weight: 300;
    letter-spacing: 15.5px;
    margin-right: -15.5px;
    line-height: 20px;
    margin-top: -2px;
  }
  .rule { height: 1px; background: var(--rule); margin: 3px 0 4px; }
  .license {
    font-size: 13.5px; font-weight: 300; letter-spacing: 0.6px;
    line-height: 18px;
    color: var(--ink-soft);
  }
  .contact {
    display: flex; justify-content: center; align-items: center; gap: 6px;
    font-size: 13.5px; font-weight: 300; letter-spacing: 0.6px;
    line-height: 22px;
    color: var(--ink-soft);
    white-space: nowrap;
  }
  .contact__icon { width: 13px; height: 10px; fill: var(--ink-soft); }
  .contact__sep { margin: 0 5px; }
</style>
</head>
<body>
<main class="sheet">
  <section class="card card--top">
    <div class="identity">
      <h1 class="name"><span class="name__first">Caldwell</span> <span class="name__last">Prusinski</span></h1>
      <p class="title">ARCHITECT</p>
      <div class="rule"></div>
      <p class="license">NY License No. 582163</p>
      <p class="contact">
        <svg class="contact__icon" viewBox="0 0 13 10" aria-hidden="true"><path d="M1 3.2C1 1.8 3.5 1 6.5 1S12 1.8 12 3.2V4H9.2V2.9H3.8V4H1z"/><path d="M3 4.6h7l2 4.4H1z"/></svg>
        <span>607 394 2858</span>
        <span class="contact__sep">|</span>
        <svg class="contact__icon" viewBox="0 0 13 10" aria-hidden="true"><path d="M1 1.5h11v7H1z"/><path d="M1.5 2l5 4 5-4" fill="none" stroke="#2f3f82" stroke-width="1"/></svg>
        <span>caldwell@designcpx.com</span>
      </p>
    </div>
  </section>
  <section class="card card--bottom">
    <div class="identity">
      <h2 class="name"><span class="name__first">Caldwell</span> <span class="name__last">Prusinski</span></h2>
      <p class="title">ARCHITECT</p>
      <div class="rule"></div>
      <p class="license">NY License No. 582163</p>
      <p class="contact">
        <svg class="contact__icon" viewBox="0 0 13 10" aria-hidden="true"><path d="M1 3.2C1 1.8 3.5 1 6.5 1S12 1.8 12 3.2V4H9.2V2.9H3.8V4H1z"/><path d="M3 4.6h7l2 4.4H1z"/></svg>
        <span>607 394 2858</span>
        <span class="contact__sep">|</span>
        <svg class="contact__icon" viewBox="0 0 13 10" aria-hidden="true"><path d="M1 1.5h11v7H1z"/><path d="M1.5 2l5 4 5-4" fill="none" stroke="#2f3f82" stroke-width="1"/></svg>
        <span>caldwell@designcpx.com</span>
      </p>
    </div>
  </section>
</main>
</body>
</html>
```